BOLD & MINIMALIST DESIGN NEEDED

We want a very bold but minimalistic business card design that is impactful and utilizes both sides of the business card. Our current logo is included for your use.

We want bold fonts and good use of negative space. We don't want the logo to overpower the design.

Target Market(s)

Professionals who are building new commercial buildings.

Industry/Entity Type

Construction

Contact Information for Business Card

Name, Title, email, office phone, cell phone, website

Font styles to use
Serif
Sans Serif

Requirements
Must have
• Bold design!

```html
<!DOCTYPE html>
<html lang="en">
<head>
<meta charset="utf-8">
<title>Ridgeline Design + Build — Business Card</title>
<link rel="stylesheet" href="https://fonts.googleapis.com/css2?family=Montserrat:wght@800&family=Fira+Sans:wght@400&display=swap">
<style>
  :root {
    --backdrop: #1e1e1e;
    --card-dark: #1b1b1b;
    --card-light: #ffffff;
    --ink: #111111;
    --ink-soft: #2a2a2a;
    --paper-text: #f2f2f2;
    --accent: #7cc52e;
  }
  * { box-sizing: border-box; margin: 0; padding: 0; }
  html, body { width: 1200px; height: 1122px; overflow: hidden; }
  body {
    background: var(--backdrop);
    font-family: "Fira Sans", sans-serif;
    position: relative;
  }
  .card {
    position: absolute;
    left: 240px;
    width: 720px;
    height: 412px;
    border-radius: 34px;
    overflow: hidden;
  }
  .card--front { top: 96px; background: var(--card-dark); }
  .card--back { top: 614px; background: var(--card-light); }

  .brand {
    display: flex;
    align-items: center;
    gap: 14px;
    font-family: "Montserrat", sans-serif;
    font-weight: 800;
    letter-spacing: 0.5px;
  }
  .brand__mark { width: 22px; height: 22px; background: var(--accent); flex: none; }
  .brand__name { font-size: 30px; line-height: 1.15; }

  .card--front .brand {
    position: absolute; inset: 0; justify-content: center;
  }
  .card--front .brand__name { color: var(--paper-text); font-size: 38px; }

  .card--back .brand {
    position: absolute; left: 52px; top: 172px; width: 290px;
  }
  .card--back .brand__name { color: var(--ink); }

  .divider {
    position: absolute; left: 360px; top: 96px;
    width: 2px; height: 220px; background: var(--ink);
  }
  .contact { position: absolute; left: 392px; top: 104px; color: var(--ink-soft); }
  .contact__name {
    font-family: "Montserrat", sans-serif; font-weight: 800;
    font-size: 30px; color: var(--ink); letter-spacing: 0.5px;
  }
  .contact__title { font-size: 19px; color: var(--accent); margin: 2px 0 16px; }
  .contact__list { list-style: none; }
  .contact__item {
    display: flex; align-items: center; gap: 12px;
    font-size: 18px; line-height: 1.75;
  }
  .contact__icon { width: 16px; height: 16px; flex: none; fill: var(--accent); }
</style>
</head>
<body>
  <section class="card card--front" aria-label="Card front">
    <div class="brand">
      <span class="brand__mark"></span>
      <span class="brand__name">RIDGELINE DESIGN + BUILD</span>
    </div>
  </section>

  <section class="card card--back" aria-label="Card back">
    <div class="brand">
      <span class="brand__mark"></span>
      <span class="brand__name">RIDGELINE DESIGN + BUILD</span>
    </div>
    <div class="divider"></div>
    <div class="contact">
      <h1 class="contact__name">MARCUS HALE</h1>
      <p class="contact__title">Founder &amp; CEO</p>
      <ul class="contact__list">
        <li class="contact__item">
          <svg class="contact__icon" viewBox="0 0 16 16" aria-hidden="true"><path d="M3.5 1l2.4 3-1.4 1.6c.8 1.9 2.3 3.4 4.2 4.2l1.6-1.4 3 2.4-1.2 2.7C7 13.4 2.6 9 1 3.2z"/></svg>
          <span>(123) 456-7890</span>
        </li>
        <li class="contact__item">
          <svg class="contact__icon" viewBox="0 0 16 16" aria-hidden="true"><path d="M4 1h8a1 1 0 0 1 1 1v12a1 1 0 0 1-1 1H4a1 1 0 0 1-1-1V2a1 1 0 0 1 1-1zm1 2v9h6V3zm3 10a.8.8 0 1 0 0 1.6A.8.8 0 0 0 8 13z"/></svg>
          <span>(123) 456-7890</span>
        </li>
        <li class="contact__item">
          <svg class="contact__icon" viewBox="0 0 16 16" aria-hidden="true"><path d="M1 3h14v10H1zm1.5 1.2V5l5.5 4 5.5-4v-.8z"/></svg>
          <span>info@ridgelinebuild.com</span>
        </li>
        <li class="contact__item">
          <svg class="contact__icon" viewBox="0 0 16 16" aria-hidden="true"><path d="M8 1a7 7 0 1 0 0 14A7 7 0 0 0 8 1zm0 1.6a5.4 5.4 0 0 1 0 10.8 5.4 5.4 0 0 1 0-10.8zM5 5h3v2H6v3H4.5A4 4 0 0 1 5 5zm4 4h2.5A4 4 0 0 1 9 12z"/></svg>
          <span>ridgelinebuild.com</span>
        </li>
      </ul>
    </div>
  </section>
</body>
</html>
```